Business Card Design Project : Tidewell Press

In preparation for market launch, Whistler's Tidewell Press require the development of a business card. Tidewell Press is a Community online publishing web portal. We provide the the city of Whistler located in B.C. (Canada) business directories, News, Classified ads, News, Events and blogs etc.

The main focus of the brand is to help local businesses to corporate with their online advertisement and marketing. Meeting our clients face to face is a must (B2B).

Target Market(s)

The target market is B2B customers. Business Owners to Marketing, advertising Managers

Industry/Entity Type

Business

Requirements
Must have
• - The business card will be two sided.
the BACK side will have our logo which consist of (icon, url,slogan) submited. The logo will be middle and centred.

The FRONT side should have company details:

Company Legal Name: FERNDALE TIDEWELL PRESS

Owen Marsk
Director of Sales & Marketing

www.ferndaletidewell.biz
owen@ferndaletidewell.biz

Phone: 555 014 3826
#2817 - 562 E. Harlow Ave.
Vancouver, B.C. K7P2R4 Canada
Nice to have
• - For the "FRONT" side of our business card. You can separate or re-arrange with our logo components (icon, logo,slogan). It does not have to be together.

Also our company legal name is rather long so arrange or organize the name in a way to make it shorter. Your experience and creativity will have to come in play.
Should not have
• should not have other colors beside logo color and black text (2 colors). Also nothing Three dimensional

```html
<!DOCTYPE html>
<html lang="en">
<head>
<meta charset="utf-8">
<title>Ferndale Tidewell Press — Business Card</title>
<link href="https://fonts.googleapis.com/css2?family=Open+Sans:wght@400;600;700&display=swap" rel="stylesheet">
<style>
  :root {
    --brand-blue: #2a7fc9;
    --ink: #0b0b0c;
    --paper: #ffffff;
    --stage: #e9e6e1;
    --muted-white: #f2f2f2;
  }
  * { margin: 0; padding: 0; box-sizing: border-box; }
  html, body {
    width: 1200px; height: 900px; overflow: hidden;
    background: var(--stage);
    font-family: "Open Sans", Arial, sans-serif;
  }
  .stage { position: relative; width: 1200px; height: 900px; }
  .card {
    position: absolute; left: 250px; width: 700px; height: 400px;
    overflow: hidden;
  }
  .card--back { top: 40px; background: var(--ink); }
  .card--front { top: 460px; background: var(--paper); }
  .card__shapes { position: absolute; inset: 0; }

  .brand { position: absolute; display: flex; align-items: center; gap: 14px; }
  .brand__mark { width: 34px; height: 34px; background: var(--brand-blue); flex: none; }
  .brand__name { font-weight: 700; letter-spacing: 0.5px; white-space: nowrap; }
  .brand__slogan { color: var(--brand-blue); font-weight: 400; white-space: nowrap; }

  .card--back .brand { left: 0; right: 0; top: 150px; justify-content: center; }
  .card--back .brand__mark { width: 48px; height: 48px; }
  .card--back .brand__name { color: var(--paper); font-size: 30px; line-height: 1.1; }
  .card--back .brand__slogan { font-size: 25px; line-height: 1.2; }

  .card--front .brand { left: 270px; top: 95px; }
  .card--front .brand__name { color: var(--ink); font-size: 22px; line-height: 1.1; }
  .card--front .brand__slogan { font-size: 19px; line-height: 1.2; }

  .url {
    position: absolute; color: var(--paper); font-size: 15px; font-weight: 600;
    white-space: nowrap; line-height: 20px;
  }
  .card--back .url { right: 24px; bottom: 10px; }
  .card--front .url { right: 22px; top: 222px; }

  .person { position: absolute; left: 40px; top: 222px; }
  .person__name { font-size: 21px; font-weight: 700; color: var(--ink); letter-spacing: 0.5px; }
  .person__title { font-size: 16px; font-weight: 600; color: var(--brand-blue); }

  .contacts { position: absolute; left: 44px; top: 305px; list-style: none; color: var(--muted-white); font-size: 15px; }
  .contacts li { display: flex; align-items: center; gap: 12px; height: 27px; white-space: nowrap; }
  .contacts svg { width: 14px; height: 14px; fill: var(--muted-white); flex: none; }
</style>
</head>
<body>
<main class="stage">

  <section class="card card--back" aria-label="Business card back">
    <svg class="card__shapes" viewBox="0 0 700 400" aria-hidden="true">
      <polygon points="460,362 700,362 700,400 445,400" fill="var(--brand-blue)"/>
    </svg>
    <div class="brand">
      <span class="brand__mark"></span>
      <div>
        <div class="brand__name">FERNDALE TIDEWELL PRESS</div>
        <div class="brand__slogan">Your information gateway</div>
      </div>
    </div>
    <div class="url">www.ferndaletidewell.biz</div>
  </section>

  <section class="card card--front" aria-label="Business card front">
    <svg class="card__shapes" viewBox="0 0 700 400" aria-hidden="true">
      <polygon points="40,292 500,292 535,180 700,180 700,400 16,400" fill="var(--ink)"/>
      <polygon points="28,292 38,292 14,400 4,400" fill="var(--brand-blue)"/>
      <polygon points="464,212 700,212 700,252 452,252" fill="var(--brand-blue)"/>
    </svg>
    <div class="brand">
      <span class="brand__mark"></span>
      <div>
        <div class="brand__name">FERNDALE TIDEWELL PRESS</div>
        <div class="brand__slogan">Your information gateway</div>
      </div>
    </div>
    <div class="url">www.ferndaletidewell.biz</div>
    <div class="person">
      <div class="person__name">OWEN MARSK</div>
      <div class="person__title">Director of Sales &amp; Marketing</div>
    </div>
    <ul class="contacts">
      <li>
        <svg viewBox="0 0 16 16" aria-hidden="true"><path d="M8 1 1 7.5h2V15h4v-4h2v4h4V7.5h2z"/></svg>
        #2817 - 562 E. Harlow Ave. Vancouver, B.C. K7P2R4 Canada
      </li>
      <li>
        <svg viewBox="0 0 16 16" aria-hidden="true"><path d="M3.5 1 6 4.5 4.6 6.3c.9 2 2.4 3.6 4.4 4.6l1.8-1.4L14.5 12l-1.6 2.6C7.5 14.8 1.2 8.5 1.4 2.9z"/></svg>
        555 014 3826
      </li>
      <li>
        <svg viewBox="0 0 16 16" aria-hidden="true"><path d="M1 3h14v10H1zm1.5 1.2L8 8.6l5.5-4.4z"/></svg>
        owen@ferndaletidewell.biz
      </li>
    </ul>
  </section>

</main>
</body>
</html>
```